Birchwater Ridge Electrical, needs business cards asap!

An electrical business, been in the trade for 10 to 12 years. Based on a partner business, names Dale Brixworth and Rk Tolly. Would like a potential logo drawn up to use on all products as well. It's a new company starting in the spring.
This is my first time using this site to make business cards. I can tell you a little about the business, I have been working as an electrician for 10 years for a company and have done courses to upgrade my skills, I'm open minded, and am very personable. Over the years I just have had it working for "the man" and want to try it on my own. I am extremely hard worker I work long hours.

again anything is so appreciative,

Thank you

Dale

Target Market(s)

Small town, contractors, other business owners,

Industry/Entity Type

Electrical

Contact Information for Business Card

Simple but classy

Font styles to use
Serif

Colors
ffc214
000000

Requirements
Must have
• Phone 555-418-9356
• Email birchwaterridgeelectrical@voltmail.test
• Address 14 Fenwick street parry sound on p2a 3k9
• Name of company ridge birchwater electrical
• Name of owners Dale Brixworth and rk tolly
• ECRA/ESA 4386192
Nice to have
• A potential logo which can be used on clothing trucks etc if no logo thats ok.

```html
<!DOCTYPE html>
<html lang="en">
<head>
<meta charset="utf-8">
<title>Birchwater Ridge Electrical — Business Card</title>
<link rel="stylesheet" href="https://fonts.googleapis.com/css2?family=Nunito+Sans:wght@400;600;900&display=swap">
<style>
  :root {
    --backdrop: #e4e4e4;
    --card-yellow: #ffc214;
    --ink: #000000;
  }
  * { box-sizing: border-box; margin: 0; padding: 0; }
  html, body {
    width: 1200px;
    height: 900px;
    overflow: hidden;
    background: var(--backdrop);
  }
  .stage {
    position: relative;
    width: 1200px;
    height: 900px;
  }
  .business-card {
    position: absolute;
    left: 240px;
    top: 244px;
    width: 720px;
    height: 412px;
    background: var(--card-yellow);
    color: var(--ink);
    font-family: "Nunito Sans", "Helvetica Neue", Arial, sans-serif;
  }
  .wordmark {
    position: absolute;
    left: 44px;
    top: 36px;
    font-weight: 900;
    font-size: 58px;
    line-height: 0.86;
    letter-spacing: -2px;
    text-transform: uppercase;
  }
  .wordmark-line { display: block; white-space: nowrap; }
  .wordmark-dot {
    display: inline-block;
    width: 14px;
    height: 14px;
    border-radius: 50%;
    background: var(--ink);
    margin-left: 8px;
    vertical-align: baseline;
  }
  .contact {
    position: absolute;
    right: 44px;
    top: 238px;
    text-align: right;
  }
  .owners {
    font-weight: 600;
    font-size: 22px;
    margin-bottom: 22px;
  }
  .contact-line {
    font-weight: 400;
    font-size: 14px;
    line-height: 1.5;
  }
</style>
</head>
<body>
  <main class="stage">
    <section class="business-card" aria-label="Birchwater Ridge Electrical business card">
      <h1 class="wordmark">
        <span class="wordmark-line">Birchwater</span>
        <span class="wordmark-line">Ridge</span>
        <span class="wordmark-line">Electrical<span class="wordmark-dot" aria-hidden="true"></span></span>
      </h1>
      <div class="contact">
        <p class="owners">Dale Brixworth &amp; Rk Tolly</p>
        <p class="contact-line">555-418-9356</p>
        <p class="contact-line">BirchwaterRidgeElectrical@Voltmail.test</p>
        <p class="contact-line">14 Fenwick St Alder Bay, ON X0Z 3K9</p>
        <p class="contact-line">ECRA/ESA 4386192</p>
      </div>
    </section>
  </main>
</body>
</html>
```